Digital Product Store Front for Educational Leaders (PraisewithPellar)

I am an a Principal, Author and Education consultant I am in need of a wordpress website that fits my brand that I will be able to sell digital products I have created, digital courses I have created, and offer mentorship and coaching services. I have my branding documents and my content/wording in the files. This website should be professional yet relatable. I'd like it to be clean, easy to navigate and be very obvious with its purpose. Please view the attached documents to give a much clearer idea about my brand and wants. :)

Target Market(s)

Educational Leaders (Principals)

Industry/Entity Type

Educational Leadership

Coding

Coded - Design and coding required

Number of Pages Required

1 page

Font styles to use
Other font styles liked:
• please use my branding font

Requirements
Must have
• All the items I listed on my document, my brand colors and font, The content I submitted is still in a very draft format but just to give the designer and idea.

```html
<!DOCTYPE html>
<html lang="en">
<head>
<meta charset="utf-8">
<title>PraisewithPellar — Educational Leadership</title>
<link rel="stylesheet" href="https://fonts.googleapis.com/css2?family=Poppins:wght@300;400;500;600&display=swap">
<style>
  :root{
    --teal:#5b9d91;
    --teal-dark:#4f8f83;
    --teal-soft:#a9cbc3;
    --teal-mist:#d7e8e3;
    --cream:#f4ede1;
    --cream-deep:#e6dac4;
    --ink:#2f3434;
    --ink-soft:#555b5a;
    --white:#ffffff;
  }
  *{box-sizing:border-box;margin:0;padding:0}
  html,body{width:1200px;height:4902px;overflow:hidden}
  body{position:relative;background:var(--white);font-family:"Poppins",sans-serif;color:var(--ink)}
  .abs{position:absolute}
  .btn{position:absolute;display:flex;align-items:center;justify-content:center;font-family:"Poppins",sans-serif;font-size:16px;font-weight:500;letter-spacing:1px;text-transform:uppercase;color:var(--white);background:var(--teal)}
  .btn--cream{background:var(--cream);color:var(--teal)}
  .btn--soft{background:var(--teal-soft)}
  .heading{position:absolute;font-weight:400;text-transform:uppercase;color:var(--teal);letter-spacing:1px;line-height:1.15;white-space:nowrap}
  .copy{position:absolute;font-size:17px;line-height:1.9;color:var(--ink)}
  .photo{position:absolute}
  .wordmark{position:absolute;font-size:34px;font-weight:500;letter-spacing:10px;color:var(--teal)}
  .site-header{position:absolute;left:0;top:0;width:1200px;height:86px;background:var(--white)}
  .nav{position:absolute;top:34px;display:flex;font-size:15px;font-weight:500;letter-spacing:.5px}
  .nav a{color:var(--ink);text-decoration:none;position:absolute;white-space:nowrap}
  .hero{position:absolute;left:0;top:86px;width:1200px;height:620px;background:#f6f6f4;overflow:hidden}
  .service{position:absolute;top:772px;width:316px;height:182px;border:1px solid #d8dcdb;background:var(--white);text-align:center}
  .service--active{background:var(--teal);border-color:var(--teal);box-shadow:0 10px 24px rgba(0,0,0,.15)}
  .service__icon{position:absolute;left:112px;top:-36px;width:90px;height:90px;border-radius:50%;background:var(--cream);border:6px solid var(--white)}
  .service__title{position:absolute;left:0;top:70px;width:100%;font-size:20px;letter-spacing:1px;color:var(--teal);text-transform:uppercase}
  .service--active .service__title{color:var(--white)}
  .band-teal{position:absolute;left:0;width:1200px;background:var(--teal)}
  .rule{position:absolute;width:84px;height:2px;background:var(--teal-soft)}
  .rule-dot{position:absolute;width:10px;height:10px;background:var(--teal)}
</style>
</head>
<body>

<header class="site-header">
  <div class="wordmark" style="left:116px;top:14px;font-size:40px;letter-spacing:12px;">PWP</div>
  <div class="abs" style="left:118px;top:62px;font-size:7px;letter-spacing:3px;color:var(--teal);">PRAISEWITHPELLAR</div>
  <nav class="nav">
    <a style="left:349px">SHOP</a>
    <a style="left:456px">LEARN</a>
    <a style="left:566px">PARTNER</a>
    <a style="left:694px">BOOK</a>
    <a style="left:801px">MEET ME</a>
  </nav>
  <div class="btn btn--soft" style="left:926px;top:26px;width:158px;height:42px;font-size:14px;">Contact Me</div>
</header>

<section class="hero">
  <div class="photo" role="img" aria-label="Smiling educator in a white sweater leaning on a desk beside a blush laptop, glasses and a potted palm" style="left:540px;top:0;width:660px;height:560px;background:linear-gradient(135deg,#f3f1ec 0%,#ece4dc 45%,#e9cfc0 75%,#f1efe9 100%)"></div>
  <svg class="abs" style="left:0;top:520px" width="1200" height="100" aria-hidden="true">
    <path d="M0 40 C300 110 700 20 1200 70 L1200 100 L0 100 Z" fill="var(--white)"/>
    <path d="M520 90 C800 40 1000 40 1200 70 L1200 100 C1000 70 800 70 520 100 Z" fill="var(--teal-soft)"/>
  </svg>
  <h1 class="heading" style="left:116px;top:142px;font-size:42px;font-weight:300;letter-spacing:1.5px;">Your school can<br>absolutely thrive.</h1>
  <p class="copy" style="left:120px;top:254px;width:450px;font-size:16px;line-height:1.85;">Let's partner together to revolutionize your school's culture into an engaged, high-performing community where everyone belongs.</p>
  <div class="btn" style="left:122px;top:362px;width:186px;height:52px;">Why Wait?</div>
  <svg class="abs" style="left:318px;top:356px" width="160" height="50" aria-hidden="true">
    <path d="M4 30 C40 46 100 46 150 12" fill="none" stroke="var(--teal)" stroke-width="1.5" stroke-dasharray="4 4"/>
    <path d="M140 8 L152 10 L148 22" fill="none" stroke="var(--teal)" stroke-width="2"/>
  </svg>
</section>

<div class="service" style="left:113px">
  <div class="service__icon"></div>
  <div class="service__title">Digital Tools</div>
  <div class="btn" style="left:86px;top:108px;width:146px;height:40px;font-size:14px;">Shop</div>
</div>
<div class="service service--active" style="left:453px;top:770px">
  <div class="service__icon"></div>
  <div class="service__title">Innovatice Courses</div>
  <div class="btn btn--cream" style="left:80px;top:108px;width:146px;height:40px;font-size:14px;">Learn</div>
</div>
<div class="service" style="left:793px">
  <div class="service__icon"></div>
  <div class="service__title">Authentic Coaching</div>
  <div class="btn" style="left:86px;top:112px;width:146px;height:40px;font-size:14px;">Partner</div>
</div>

<div class="abs" style="left:116px;top:1052px;width:372px;height:360px;background:var(--cream)"></div>
<div class="abs" style="left:120px;top:1330px;font-size:32px;font-weight:300;letter-spacing:4px;color:var(--cream-deep);transform:rotate(-90deg);transform-origin:left top;white-space:nowrap;">DIGITAL</div>
<div class="abs" style="left:144px;top:1070px;width:438px;height:382px;border:1px solid var(--teal-soft)"></div>
<div class="photo" role="img" aria-label="Hands typing on a rose-gold laptop beside a notebook and reading glasses" style="left:156px;top:1080px;width:416px;height:360px;background:linear-gradient(160deg,#f7f7f5 0%,#e7e4de 50%,#cfc7bd 100%)"></div>
<h2 class="heading" style="left:648px;top:1102px;font-size:36px;">Digital Tools</h2>
<p class="copy" style="left:650px;top:1160px;width:450px;font-size:18px;line-height:1.75;">From staff and student events, to ___ these digital tools are just one File. Print. away from revolutionalizing your school culture.</p>
<p class="copy" style="left:650px;top:1258px;width:460px;font-size:15px;">(Printed in color of course) (Get that color ink ready!)</p>
<div class="btn" style="left:652px;top:1320px;width:188px;height:52px;">Why Wait?</div>

<section class="band-teal" style="top:1512px;height:554px;overflow:hidden">
  <div class="abs" style="left:996px;top:56px;width:154px;height:154px;border-radius:50%;background:var(--cream)"></div>
  <h2 class="heading" style="left:130px;top:124px;font-size:35px;color:var(--white);">Innovatice Courses</h2>
  <p class="copy" style="left:130px;top:180px;width:470px;font-size:18px;line-height:1.78;color:var(--white);">Join an individual or team online training course designed to elevate your leadership skills, revolutionize your school culture or transform student behvaior. (And you can even say you thought of it yourself) IDK something at the end</p>
  <div class="btn btn--cream" style="left:132px;top:400px;width:188px;height:52px;font-weight:400;">Learn</div>
  <svg class="abs" style="left:344px;top:388px" width="150" height="44" aria-hidden="true">
    <path d="M2 20 C40 6 90 40 140 12" fill="none" stroke="var(--white)" stroke-width="1.5" stroke-dasharray="4 4"/>
    <path d="M130 6 L142 10 L136 20" fill="none" stroke="var(--white)" stroke-width="2"/>
  </svg>
  <div class="photo" role="img" aria-label="Desktop monitor showing an online course library with four course cards" style="left:630px;top:100px;width:472px;height:372px;background:linear-gradient(180deg,#1f2424 0%,#1f2424 74%,#d9dcdb 74%,#c8cccb 100%);border-radius:8px"></div>
</section>

<div class="photo" role="img" aria-label="Two women in conversation on a blush sofa against a white brick wall, one taking notes" style="left:0;top:2066px;width:622px;height:554px;background:linear-gradient(135deg,#efefec 0%,#e2ddd8 45%,#c7a59c 80%,#b8948a 100%)"></div>
<div class="abs" style="left:574px;top:2190px;width:544px;height:310px;background:var(--white);box-shadow:0 8px 30px rgba(0,0,0,.06)"></div>
<h2 class="heading" style="left:634px;top:2234px;font-size:30px;">Authentic Coaching</h2>
<p class="copy" style="left:635px;top:2282px;width:440px;font-size:14.5px;line-height:2.2;">Unleash your leadership potential in this mentorship experience as we work together to curate a personalized plan to (Let's Be Smart Friends!)</p>
<div class="btn" style="left:636px;top:2400px;width:188px;height:52px;">Why Wait?</div>

<section class="abs" style="left:0;top:2620px;width:1200px;height:560px;background:linear-gradient(180deg,var(--cream) 0%,#f4ede1 60%,#efe4d1 100%)">
  <div class="abs" style="left:140px;top:86px;width:170px;height:170px;border-radius:50%;background:var(--teal)"></div>
  <div class="photo" role="img" aria-label="Book cover: Culture Comes First by Pellar Whitford, with the author seated on the cover" style="left:200px;top:80px;width:252px;height:396px;background:linear-gradient(180deg,#fbfaf7 0%,#efe8de 55%,#e4dccf 100%);box-shadow:6px 10px 20px rgba(0,0,0,.18)"></div>
  <svg class="abs" style="left:478px;top:360px" width="130" height="50" aria-hidden="true">
    <path d="M124 8 C90 40 50 44 10 30" fill="none" stroke="var(--teal)" stroke-width="1.5" stroke-dasharray="4 4"/>
    <path d="M20 22 L8 30 L18 40" fill="none" stroke="var(--teal)" stroke-width="2"/>
  </svg>
  <h2 class="heading" style="left:612px;top:96px;font-size:40px;font-weight:300;">Shop Book</h2>
  <div class="rule" style="left:614px;top:156px"></div>
  <div class="rule-dot" style="left:614px;top:152px"></div>
  <p class="copy" style="left:612px;top:180px;width:500px;font-size:16.5px;line-height:1.85;">The most important tool in connecting your community and creating a high-performing, thriving culture is YOU! Enhance your people-centered leadership style and learn the #1 Rules of growing your culture.</p>
  <p class="copy" style="left:612px;top:306px;width:520px;font-size:16.5px;line-height:1.85;">Begin this process today by ordering an ReadMart<br>#1 New Release: <b>Culture Comes First</b></p>
  <div class="btn" style="left:612px;top:380px;width:176px;height:50px;">Buy Now</div>
</section>

<section class="abs" style="left:106px;top:3126px;width:984px;height:294px;border-radius:34px 0 34px 0;background:linear-gradient(90deg,var(--teal) 0%,#74aea3 55%,#b6d3cc 100%)">
  <h2 class="heading" style="left:72px;top:60px;font-size:26px;color:var(--white);letter-spacing:.5px;line-height:1.3;">Sign-up for the<br>PraisewithPellar Newsletter</h2>
  <p class="abs" style="left:72px;top:136px;font-size:15px;color:var(--white);">Who doesn't want more emails?</p>
  <div class="abs" style="left:72px;top:172px;width:420px;height:50px;background:var(--white);box-shadow:0 4px 10px rgba(0,0,0,.12)"></div>
  <p class="abs" style="left:100px;top:189px;font-size:13px;color:var(--ink);">Your Email address</p>
  <div class="btn" style="left:368px;top:178px;width:118px;height:38px;font-size:11px;font-weight:600;">Subscribe</div>
  <svg class="abs" style="left:505px;top:140px" width="110" height="40" aria-hidden="true">
    <path d="M2 20 C30 40 70 36 100 20" fill="none" stroke="var(--white)" stroke-width="1.5" stroke-dasharray="4 4"/>
    <path d="M92 14 L102 20 L94 28" fill="none" stroke="var(--white)" stroke-width="2"/>
  </svg>
  <div class="photo" role="img" aria-label="Laptop showing the newsletter sign-up screen" style="left:620px;top:40px;width:300px;height:212px;background:linear-gradient(180deg,#2a2e2e 0%,#2a2e2e 84%,#cfd3d2 84%,#b8bcbb 100%);border-radius:10px"></div>
</section>

<h2 class="heading" style="left:130px;top:3510px;font-size:46px;font-weight:300;">About</h2>
<div class="rule" style="left:132px;top:3576px"></div>
<div class="rule-dot" style="left:132px;top:3572px"></div>
<p class="copy" style="left:130px;top:3596px;width:510px;font-size:15.5px;line-height:1.68;">(Why, hello there!) Welcome to PraisewithPellar! I am Pellar Whitford an Elementary Principal in Brookfield, Vermont, Author of Culture Comes First, and Education Consultant. I am super passionate about bringing change to the way school leaders serve –both children and adults.</p>
<p class="copy" style="left:130px;top:3752px;width:510px;font-size:15.5px;line-height:1.68;">I was a teacher for eight years, and then an instructional coach, before earning my dream job as a elementary school principal! I am now in my sixth year as a school leader and have dramatically shifted the traditional elementary school culture into a thriving, loving community</p>
<div class="btn" style="left:130px;top:3904px;width:186px;height:50px;font-weight:400;">Contact Me</div>
<svg class="abs" style="left:490px;top:3890px" width="160" height="50" aria-hidden="true">
  <path d="M150 6 C110 40 60 44 14 30" fill="none" stroke="var(--teal)" stroke-width="1.5" stroke-dasharray="4 4"/>
  <path d="M24 20 L10 30 L22 40" fill="none" stroke="var(--teal)" stroke-width="2"/>
</svg>
<div class="abs" style="left:688px;top:3512px;width:414px;height:464px;background:var(--teal-mist);border-radius:207px 207px 0 0"></div>
<div class="abs" style="left:666px;top:3490px;width:414px;height:464px;border:2px solid var(--teal-mist);border-radius:207px 207px 0 0;background:var(--white)"></div>
<div class="photo" role="img" aria-label="Cheerful author in a cream knit sweater gesturing playfully" style="left:676px;top:3500px;width:394px;height:444px;border-radius:197px 197px 0 0;background:linear-gradient(160deg,#f7f6f3 0%,#ece6dd 55%,#ddd2c3 100%)"></div>

<section class="abs" style="left:0;top:4060px;width:1200px;height:620px;overflow:hidden">
  <svg class="abs" style="left:0;top:0" width="1200" height="620" aria-hidden="true">
    <path d="M0 90 C300 30 700 140 1200 70 L1200 620 L0 620 Z" fill="var(--teal)"/>
  </svg>
  <div class="photo" role="img" aria-label="Author in glasses and a white sweater holding a notebook, smiling" style="left:150px;top:14px;width:360px;height:606px;background:linear-gradient(180deg,#f4f2ee 0%,#e8e3db 50%,#dcd5ca 100%);border-radius:180px 180px 0 0"></div>
  <h2 class="heading" style="left:540px;top:182px;font-size:36px;font-weight:300;color:var(--white);">A message from Pellar</h2>
  <div class="rule" style="left:542px;top:232px"></div>
  <div class="rule-dot" style="left:542px;top:228px;background:var(--white)"></div>
  <p class="copy" style="left:540px;top:248px;width:570px;font-size:13px;line-height:1.85;color:var(--white);">I am so happy you are here! (Seriously!) Working with other educational leaders brings me THE. MOST. JOY. (I'm OBSESSED)<br>I want to support you on every inch of your journey! We can work alongside each other to navigate the challenges of leading adults, transforming student behaviors, and creating a vibrant atmosphere.<br>School leadership can be lonely, taxing, and overwhelming. Often, the biggest challenge is knowing where to start as you face the pressures and demands from the many stakeholders.<br>But don't worry, I can't wait to help you! So whether you need tools to enhance your own leadership skills, to facilitate connection within your community, or to transform student behaviors, I am here to help you develop your school into a high-performing culture. Let's get started today!!</p>
</section>

<footer class="abs" style="left:0;top:4680px;width:1200px;height:222px;background:var(--white)">
  <div class="wordmark" style="left:144px;top:28px;font-size:38px;letter-spacing:12px;">PWP</div>
  <div class="abs" style="left:146px;top:74px;font-size:7px;letter-spacing:3px;color:var(--teal);">PRAISEWITHPELLAR</div>
  <nav class="nav" style="top:56px">
    <a style="left:373px">SHOP</a>
    <a style="left:481px">LEARN</a>
    <a style="left:590px">PARTNER</a>
    <a style="left:720px">BOOK</a>
    <a style="left:826px">MEET ME</a>
    <a style="left:951px">CONTACT ME</a>
  </nav>
  <div class="abs" style="left:0;top:104px;width:1200px;height:1px;background:#e4e7e6"></div>
  <p class="abs" style="left:140px;top:152px;font-size:12px;color:var(--ink-soft);">© 2024 PraisewithPellar. All Rights Reserved</p>
  <div class="abs" style="left:934px;top:134px;width:36px;height:36px;border-radius:50%;background:var(--teal-mist)"></div>
  <div class="abs" style="left:978px;top:134px;width:36px;height:36px;border-radius:50%;background:var(--teal)"></div>
  <div class="abs" style="left:1024px;top:134px;width:36px;height:36px;border-radius:50%;background:var(--teal-mist)"></div>
</footer>

</body>
</html>
```